Offshore Energy Projects Management Consultancy needs a business card design

Logo available. We provide teams to deliver engineering consultancy, project management and delivery teams mainly in the offshore renewables sector. The company is all about bringing the right people to a project to deliver the scope.

The business card will be used for all staff.

The business card should be quite simple, vibrant and uncluttered but convey experience, enthusiasm and integration.

Target Market(s)

Energy Project Developers and Tier 1 construction companies

Contact Information for Business Card

Logo should be on the back of the card. I'm happy for the designer to play with the colour of the logo and background colour.

Front of the card should convey all the must have information in a clear and professional manner but without being overly traditional.

Colors

Designer to choose colors to be used in the design.

Requirements
Must have
• Land Line Tel Number, Mobile Tel Number, Email, business address, web address.

```html
<!DOCTYPE html>
<html lang="en">
<head>
<meta charset="utf-8">
<title>Seabridge Delivery Partners – Business Card</title>
<link rel="stylesheet" href="https://fonts.googleapis.com/css2?family=Exo+2:wght@700&family=Questrial&display=swap">
<style>
  :root {
    --sky: #26a9e0;
    --navy: #1b75bb;
    --slate: #6d6e70;
    --paper: #ffffff;
    --backdrop: #e4e7eb;
  }
  * { box-sizing: border-box; margin: 0; padding: 0; }
  html, body {
    width: 1200px; height: 1200px; overflow: hidden;
    background: var(--backdrop);
  }
  .canvas { position: relative; width: 1200px; height: 1200px; }
  .card {
    position: absolute; left: 216px; width: 766px; height: 446px;
    background: var(--paper); overflow: hidden;
  }
  .card--front { top: 108px; }
  .card--back { top: 631px; }

  .accent-field {
    position: absolute; left: 0; right: 0; height: 53px;
  }
  .accent-field--top { top: 0; background: linear-gradient(90deg, var(--sky), var(--navy)); }
  .accent-field--bottom { bottom: 0; background: linear-gradient(90deg, var(--navy), var(--sky)); }

  .brand {
    position: absolute; display: flex; align-items: center;
    font-family: "Exo 2", sans-serif; font-weight: 700;
    color: var(--slate); text-transform: uppercase;
  }
  .brand__dot { border-radius: 50%; background: var(--sky); flex: none; }
  .brand__name { line-height: 1.08; }
  .brand--front { left: 0; right: 0; top: 165px; justify-content: center; gap: 18px; }
  .brand--front .brand__dot { width: 52px; height: 52px; }
  .brand--front .brand__name { font-size: 34px; }
  .brand--back { left: 30px; top: 170px; gap: 12px; }
  .brand--back .brand__dot { width: 36px; height: 36px; }
  .brand--back .brand__name { font-size: 25px; }

  .divider {
    position: absolute; left: 341px; top: 105px; width: 2px; height: 238px;
    background: var(--sky); border-radius: 1px;
  }
  .contact-list { position: absolute; left: 383px; top: 0; list-style: none; }
  .contact {
    position: absolute; left: 0; display: flex; align-items: center;
    white-space: nowrap;
  }
  .contact__icon { width: 49px; height: 46px; flex: none; }
  .contact__text {
    margin-left: 25px; font-family: "Questrial", sans-serif;
    font-size: 22px; color: var(--slate); line-height: 1.2;
  }
  .contact__text--phone { font-family: "Exo 2", sans-serif; font-weight: 700; font-size: 23px; }
  .contact--landline { top: 91px; }
  .contact--mobile { top: 142px; }
  .contact--email { top: 196px; }
  .contact--web { top: 245px; }
  .contact--address { top: 301px; }
</style>
</head>
<body>
<main class="canvas">

  <section class="card card--front" aria-label="Card front">
    <div class="accent-field accent-field--top" role="img" aria-label="Decorative blue band graphic"></div>
    <div class="brand brand--front">
      <span class="brand__dot"></span>
      <span class="brand__name">Seabridge<br>Delivery Partners</span>
    </div>
    <div class="accent-field accent-field--bottom" role="img" aria-label="Decorative blue band graphic"></div>
  </section>

  <section class="card card--back" aria-label="Card back">
    <div class="brand brand--back">
      <span class="brand__dot"></span>
      <span class="brand__name">Seabridge<br>Delivery Partners</span>
    </div>

    <div class="divider"></div>

    <ul class="contact-list">
      <li class="contact contact--landline">
        <svg class="contact__icon" viewBox="0 0 49 46" aria-hidden="true">
          <rect width="49" height="46" rx="15" fill="var(--navy)"/>
          <path fill="#fff" d="M11 17 C11 11 38 11 38 17 L38 19 L32 19 L32 16 L17 16 L17 19 L11 19 Z"/>
          <path fill="#fff" d="M15 22 L34 22 L36 34 L13 34 Z"/>
          <g fill="var(--navy)">
            <circle cx="20" cy="26" r="1.3"/><circle cx="24.5" cy="26" r="1.3"/><circle cx="29" cy="26" r="1.3"/>
            <circle cx="20" cy="30" r="1.3"/><circle cx="24.5" cy="30" r="1.3"/><circle cx="29" cy="30" r="1.3"/>
          </g>
        </svg>
        <span class="contact__text contact__text--phone">+44 20 7946 0321</span>
      </li>
      <li class="contact contact--mobile">
        <svg class="contact__icon" viewBox="0 0 49 46" aria-hidden="true">
          <rect width="49" height="46" rx="15" fill="var(--navy)"/>
          <rect x="17" y="8" width="15" height="30" rx="3" fill="none" stroke="#fff" stroke-width="2"/>
          <line x1="22" y1="34" x2="27" y2="34" stroke="#fff" stroke-width="2" stroke-linecap="round"/>
          <path fill="#fff" d="M20 17 L23 15 L25 19 L23 20.5 C24 23 25 24 27 25 L28.5 23 L32 25 L30 28 C25 28 20 23 20 17 Z"/>
        </svg>
        <span class="contact__text contact__text--phone">+44 7700 900 214</span>
      </li>
      <li class="contact contact--email">
        <svg class="contact__icon" viewBox="0 0 49 46" aria-hidden="true">
          <rect width="49" height="46" rx="15" fill="var(--navy)"/>
          <rect x="10" y="12" width="26" height="18" rx="1.5" fill="#fff"/>
          <path d="M11 13 L23 23 L35 13" fill="none" stroke="var(--navy)" stroke-width="1.8"/>
          <circle cx="36" cy="32" r="6.5" fill="#fff"/>
          <circle cx="36" cy="32" r="3.6" fill="none" stroke="var(--navy)" stroke-width="1.6"/>
        </svg>
        <span class="contact__text">hello@seabridgedp.com</span>
      </li>
      <li class="contact contact--web">
        <svg class="contact__icon" viewBox="0 0 49 46" aria-hidden="true">
          <rect width="49" height="46" rx="15" fill="var(--navy)"/>
          <circle cx="24.5" cy="23" r="14" fill="none" stroke="#fff" stroke-width="2"/>
          <ellipse cx="24.5" cy="23" rx="6" ry="14" fill="none" stroke="#fff" stroke-width="1.6"/>
          <line x1="10.5" y1="23" x2="38.5" y2="23" stroke="#fff" stroke-width="1.6"/>
        </svg>
        <span class="contact__text">www.seabridgedp.com</span>
      </li>
      <li class="contact contact--address">
        <svg class="contact__icon" viewBox="0 0 49 46" aria-hidden="true">
          <rect width="49" height="46" rx="15" fill="var(--navy)"/>
          <rect x="11" y="9" width="14" height="28" fill="none" stroke="#fff" stroke-width="2"/>
          <g stroke="#fff" stroke-width="1.6">
            <line x1="14" y1="14" x2="22" y2="14"/><line x1="14" y1="18" x2="22" y2="18"/><line x1="14" y1="22" x2="22" y2="22"/>
          </g>
          <path d="M32 38 C27 31 25 28 25 24 A7 7 0 0 1 39 24 C39 28 37 31 32 38 Z" fill="var(--navy)" stroke="#fff" stroke-width="2"/>
          <circle cx="32" cy="24" r="2.6" fill="#fff"/>
        </svg>
        <span class="contact__text">SDP House, Harbour Road,<br>Portwell, PW-30518</span>
      </li>
    </ul>
  </section>

</main>
</body>
</html>
```